Wedding Marlies & Joost - Save the Date Wedding Card

I would like to have a creative save the date wedding card. We like grey/black/white colors and modern/ plain and simple.
I like the Save the Date copy big and book a flight copy smaller. I like stylish fonts for the save the date copy
Copy front:
Save the Date & book a flight
7-10-2017 Denia (Spanje)
Marlies & Joost
Onze dag is niet compleet zonder jou!
Copy back:
6-10 preferred travel date
7-10 wedding ceremony/drinks/dinner/party
8-10 hangover breakfast
Nearest Airports Valencia & Alicante
More info will be available soon!
wedding guests
Wedding

```html
<!DOCTYPE html>
<html lang="nl">
<head>
<meta charset="utf-8">
<title>Save the Date – Marlies &amp; Joost</title>
<link rel="stylesheet" href="https://fonts.googleapis.com/css2?family=Great+Vibes&family=Cormorant+Garamond:ital,wght@0,500;1,500&family=Lato:wght@300;400;900&display=swap">
<style>
  :root {
    --backdrop: #e3e3e3;
    --card-edge: #f7f7f7;
    --border-black: #0b0b0b;
    --damask-tone: #2a2a2a;
    --panel-grey: #595959;
    --ink-white: #f5f5f5;
    --ink-soft: #e6e6e6;
  }
  * { margin: 0; padding: 0; box-sizing: border-box; }
  html, body {
    width: 1200px;
    height: 994px;
    overflow: hidden;
    background: var(--backdrop);
  }
  .stage {
    position: relative;
    width: 1200px;
    height: 994px;
  }
  .card {
    position: absolute;
    background: var(--card-edge);
    border-radius: 14px;
    padding: 6px;
    box-shadow: 0 4px 14px rgba(0,0,0,0.2);
  }
  .card-back  { left: 60px;  top: 40px;  width: 760px; height: 500px; }
  .card-front { left: 360px; top: 380px; width: 800px; height: 560px; }
  .card-border {
    position: relative;
    width: 100%;
    height: 100%;
    border-radius: 9px;
    overflow: hidden;
    background: var(--border-black);
  }
  .damask-fill {
    position: absolute;
    inset: 0;
    background:
      radial-gradient(circle at 15% 20%, var(--damask-tone) 0 6%, transparent 18%),
      radial-gradient(circle at 85% 30%, var(--damask-tone) 0 5%, transparent 16%),
      radial-gradient(circle at 25% 85%, var(--damask-tone) 0 6%, transparent 18%),
      radial-gradient(circle at 80% 80%, var(--damask-tone) 0 5%, transparent 17%),
      radial-gradient(ellipse at 50% 50%, #1c1c1c 0%, var(--border-black) 75%);
  }

  /* back side */
  .oval {
    position: absolute;
    left: 90px; right: 90px; top: 46px; bottom: 46px;
    border-radius: 50%;
    background: var(--panel-grey);
    border: 2px solid var(--ink-white);
    outline: 2px solid var(--ink-white);
    outline-offset: 5px;
    display: flex;
    flex-direction: column;
    align-items: center;
    padding-top: 62px;
    color: var(--ink-white);
    text-align: center;
    font-family: "Cormorant Garamond", serif;
    font-style: italic;
    font-weight: 500;
  }
  .schedule { font-size: 24px; line-height: 1.45; }
  .schedule-rule {
    width: 300px;
    border-top: 2px solid var(--ink-white);
    border-bottom: 1px solid var(--ink-white);
    height: 5px;
    margin: 10px 0;
  }
  .travel-note { font-size: 22px; line-height: 1.4; color: var(--ink-soft); }

  /* front side */
  .panel {
    position: absolute;
    top: 42px; left: 42px; right: 42px; bottom: 42px;
    background: var(--panel-grey);
    border: 2px solid var(--ink-white);
    outline: 2px solid var(--ink-white);
    outline-offset: 5px;
    display: flex;
    flex-direction: column;
    align-items: center;
    padding-top: 6px;
    color: var(--ink-white);
    text-align: center;
  }
  .headline {
    font-family: "Great Vibes", cursive;
    font-weight: 400;
    font-size: 108px;
    line-height: 1.05;
  }
  .ampersand {
    font-family: "Great Vibes", cursive;
    font-size: 50px;
    line-height: 0.7;
    margin-top: -6px;
  }
  .subline {
    font-family: "Cormorant Garamond", serif;
    font-weight: 500;
    font-size: 28px;
    line-height: 1.1;
    color: var(--ink-soft);
  }
  .names-block {
    margin-top: 6px;
    padding: 4px 10px;
    border-top: 2px solid var(--ink-white);
    border-bottom: 2px solid var(--ink-white);
    position: relative;
  }
  .names-block::before,
  .names-block::after {
    content: "";
    position: absolute;
    left: 0; right: 0;
    height: 1px;
    background: var(--ink-white);
  }
  .names-block::before { top: 4px; }
  .names-block::after { bottom: 4px; }
  .couple {
    font-family: "Lato", sans-serif;
    font-weight: 900;
    font-size: 46px;
    letter-spacing: 1px;
    line-height: 1.3;
  }
  .date {
    font-family: "Lato", sans-serif;
    font-weight: 900;
    font-size: 32px;
    line-height: 1.2;
    margin-top: 6px;
  }
  .place {
    font-family: "Lato", sans-serif;
    font-weight: 900;
    font-size: 36px;
    letter-spacing: 1px;
    line-height: 1.15;
  }
  .tagline {
    font-family: "Lato", sans-serif;
    font-weight: 300;
    font-size: 28px;
    line-height: 1.35;
    color: var(--ink-soft);
  }
</style>
</head>
<body>
  <main class="stage">
    <article class="card card-back">
      <div class="card-border">
        <div class="damask-fill" role="img" aria-label="Black damask floral pattern border"></div>
        <section class="oval">
          <p class="schedule">6-10 preferred travel date</p>
          <p class="schedule">7-10 ceremony | drinks | dinner | party</p>
          <p class="schedule">8-10 hangover breakfast</p>
          <div class="schedule-rule"></div>
          <p class="travel-note">Nearest airports Valencia &amp; Alicante</p>
          <p class="travel-note">More info will be available soon!</p>
        </section>
      </div>
    </article>

    <article class="card card-front">
      <div class="card-border">
        <div class="damask-fill" role="img" aria-label="Black damask floral pattern border"></div>
        <section class="panel">
          <h1 class="headline">Save the Date</h1>
          <p class="ampersand">&amp;</p>
          <p class="subline">book a flight</p>
          <div class="names-block">
            <p class="couple">MARLIES &amp; JOOST</p>
          </div>
          <p class="date">7 oktober 2017</p>
          <p class="place">DENIA, SPANJE</p>
          <p class="tagline">Onze dag is niet compleet zonder jou!</p>
        </section>
      </div>
    </article>
  </main>
</body>
</html>
```